Company Profile
Korvane Cargo Sdn Bhd is a well-established and experienced freight forwarder in Kuala Lumpur, Malaysia. We specialize in air and sea forwarding, Custom Brokerage and regulatory compliance services, inland transportation, overseas freighting and warehousing and distribution management. With our dedicated qualified and experienced professionals, we are fully committed to serving our clients.

Our Mission
Based on the motto “Quick, Reliable and Polite”, Korvane Cargo is dedicated to upholding the following three points corporate philosophy:1. Adhering to the principle that “the customer always comes first”.2. Contributing to the development of the local community.3. Making it our duty to be responsible and sincere.

Our Edge
• One-Stop Logistics Solutions
• Extensive Network Throughout Malaysia
• Highly Qualified and Experienced Pool of Professionals
• Comprehensive IT Solutions
• Innovative and Customer-focused Solutions
• Flexible and Consistent in Managing Exceptions
• Total Supply Chain Visibility

Target Market : We sell the logistics services to all the industry in Malaysia. (One Stop Logistics Solutions)

Business Card Detail : I would like to see the logo on the front with the general info.

Must Haves :
1) Name, Title, Office, Cell, Fax, Email, Address, Website
2) Must have complete company name show as : Korvane Cargo Sdn Bhd
3) Must have company registration no, show as : 8571620-W

Nice to Haves : Modern Design Business Card

Target Market(s)

We sell the logistics services to all the industry in Malaysia. (One Stop Logistics Solutions)

Contact Information for Business Card

I would like to see the logo on the front with the general info.

Colors

Designer to choose colors to be used in the design.

Requirements
Must have
• 1) Name, Title, Office, Cell, Fax, Email, Address, Website
• 2) Must have complete company name show as : Korvane Cargo Sdn Bhd
• 3) Must have company registration no, show as : 8571620-W
Nice to have
• Modern Design Business Card
Should not have
• Nil

```html
<!DOCTYPE html>
<html lang="en">
<head>
<meta charset="utf-8">
<title>Korvane Cargo – Business Card</title>
<link rel="stylesheet" href="https://fonts.googleapis.com/css2?family=Open+Sans:wght@400;600;700&display=swap">
<style>
  :root {
    --bg: #ececec;
    --card: #ffffff;
    --navy: #1b3f8f;
    --band-dark: #0d4a97;
    --band-mid: #1463ad;
    --sky-dark: #2f86c9;
    --sky-light: #5fb0e6;
    --ink: #1d2f6f;
    --icon: #111111;
  }
  * { box-sizing: border-box; margin: 0; padding: 0; }
  html, body { width: 1200px; height: 1200px; overflow: hidden; }
  body {
    background: var(--bg);
    font-family: "Open Sans", sans-serif;
    display: flex;
    flex-direction: column;
    align-items: center;
    justify-content: center;
    gap: 40px;
  }
  .card {
    position: relative;
    width: 900px;
    height: 540px;
    background: var(--card);
    box-shadow: 0 6px 22px rgba(0,0,0,0.12);
    overflow: hidden;
  }
  .wordmark {
    display: flex;
    align-items: center;
    gap: 18px;
    color: var(--navy);
    font-weight: 700;
    text-transform: uppercase;
    letter-spacing: 0.08em;
  }
  .wordmark__dot {
    border: 6px solid var(--navy);
    border-radius: 50%;
    flex: none;
  }

  /* Front */
  .card--front .wordmark { position: absolute; left: 0; right: 0; top: 130px; justify-content: center; font-size: 58px; }
  .card--front .wordmark__dot { width: 78px; height: 78px; }
  .company-name {
    position: absolute; left: 0; right: 0; top: 262px;
    text-align: center; color: var(--navy); font-size: 32px; font-weight: 400;
  }
  .tagline-band {
    position: absolute; left: 0; right: 0; bottom: 0; height: 190px;
    background: linear-gradient(100deg, var(--band-dark), var(--band-mid) 60%, #1a72b8);
    display: flex; align-items: center; justify-content: center;
    color: #fff; font-size: 40px; font-weight: 400;
  }

  /* Back */
  .card--back .wordmark { position: absolute; left: 60px; top: 190px; font-size: 36px; }
  .card--back .wordmark__dot { width: 52px; height: 52px; border-width: 5px; }
  .info-row { display: flex; align-items: flex-start; gap: 16px; color: var(--ink); font-size: 19px; line-height: 1.3; }
  .info-row svg { flex: none; width: 22px; height: 22px; margin-top: 2px; }
  .company-details { position: absolute; left: 60px; top: 300px; display: flex; flex-direction: column; gap: 26px; }
  .name-panel {
    position: absolute; left: 460px; right: 0; top: 60px; height: 145px;
    background: linear-gradient(90deg, var(--sky-dark), var(--sky-light));
    padding: 30px 0 0 44px; color: #fff;
  }
  .name-panel__name { font-size: 40px; font-weight: 600; line-height: 1.1; }
  .name-panel__title { font-size: 20px; margin-top: 4px; }
  .contact-list { position: absolute; left: 504px; top: 235px; display: flex; flex-direction: column; gap: 10px; }
  .contact-list .gap { height: 22px; }
</style>
</head>
<body>

<section class="card card--front">
  <div class="wordmark"><span class="wordmark__dot"></span><span>Korvane Cargo</span></div>
  <p class="company-name">Korvane Cargo Sdn Bhd</p>
  <div class="tagline-band">One Stop Logistics Specialist</div>
</section>

<section class="card card--back">
  <div class="wordmark"><span class="wordmark__dot"></span><span>Korvane Cargo</span></div>

  <div class="company-details">
    <div class="info-row">
      <svg viewBox="0 0 24 24" aria-hidden="true"><circle cx="12" cy="12" r="10" fill="none" stroke="var(--icon)" stroke-width="2"/><text x="12" y="16.5" text-anchor="middle" font-size="12" font-weight="700" font-family="Open Sans, sans-serif" fill="var(--icon)">R</text></svg>
      <span>8571620-W</span>
    </div>
    <div class="info-row">
      <svg viewBox="0 0 24 24" aria-hidden="true"><path d="M12 2a7 7 0 0 0-7 7c0 5 7 13 7 13s7-8 7-13a7 7 0 0 0-7-7z" fill="var(--icon)"/><circle cx="12" cy="9" r="2.6" fill="#fff"/></svg>
      <address style="font-style:normal">No.8B, 2nd Floor, Jalan Seri Indah 3/KS9,<br>Taman Seri Indah, 41300 Klang,<br>Selangor Darul Ehsan,<br>Malaysia.</address>
    </div>
  </div>

  <div class="name-panel">
    <p class="name-panel__name">Marcus Teoh</p>
    <p class="name-panel__title">Managing Director</p>
  </div>

  <div class="contact-list">
    <div class="info-row">
      <svg viewBox="0 0 24 24" aria-hidden="true"><rect x="6" y="2" width="12" height="20" rx="2" fill="none" stroke="var(--icon)" stroke-width="2"/><circle cx="12" cy="18.5" r="1" fill="var(--icon)"/></svg>
      <span>(+6012) 480 2217</span>
    </div>
    <div class="info-row">
      <svg viewBox="0 0 24 24" aria-hidden="true"><path d="M6.6 10.8a15 15 0 0 0 6.6 6.6l2.2-2.2c.3-.3.7-.4 1-.2 1.1.4 2.3.6 3.6.6.6 0 1 .4 1 1V20c0 .6-.4 1-1 1A17 17 0 0 1 3 4c0-.6.4-1 1-1h3.5c.6 0 1 .4 1 1 0 1.3.2 2.5.6 3.6.1.3 0 .7-.2 1z" fill="var(--icon)"/></svg>
      <span>(+603) 5512 7830 / 7831</span>
    </div>
    <div class="info-row">
      <svg viewBox="0 0 24 24" aria-hidden="true"><rect x="6" y="2" width="12" height="6" fill="var(--icon)"/><rect x="2" y="9" width="20" height="9" rx="2" fill="var(--icon)"/><rect x="6" y="14" width="12" height="8" fill="#fff" stroke="var(--icon)" stroke-width="2"/></svg>
      <span>(+603) 5512 7832</span>
    </div>
    <div class="gap"></div>
    <div class="info-row">
      <svg viewBox="0 0 24 24" aria-hidden="true"><rect x="2" y="5" width="20" height="14" fill="var(--icon)"/><path d="M2 5l10 8 10-8" fill="none" stroke="#fff" stroke-width="1.6"/></svg>
      <span>marcus.teoh@korvanecargo.com.my</span>
    </div>
    <div class="info-row">
      <svg viewBox="0 0 24 24" aria-hidden="true"><g fill="none" stroke="var(--icon)" stroke-width="1.8"><circle cx="12" cy="12" r="10"/><ellipse cx="12" cy="12" rx="4.5" ry="10"/><path d="M2 12h20M4 7h16M4 17h16"/></g></svg>
      <span>www.korvanecargo.com.my</span>
    </div>
  </div>
</section>

</body>
</html>
```